Thornwell Building Company - advertisement poster

I am looking to print some canvas signs to advertise my general contracting company, Thornwell Building Company. The sign will measure 6' long x 3' high so the size should match that ratio. I already have a logo icon, which is the Letter 'T' and some trees that I would like to incorporate, see attached. I would also like the to have the following information listed:
1) phone number: 472-555-0188
2) email: thornwellbuildingcompany@mailvero.com
3) website: thornwellbuildingcompany.com
4) Lic#4620385
5) I want to use this text: "BUILD WITH THE T-CREW!"

The ad should be relatively simple and clean. Black and Green are my company colors. I am open to creative ideas!

Target Market(s)

People looking to renovate their homes

Industry/Entity Type

Construction

Colors
59FF00
82FF00
B8FF75
E3FFCB
F4FFEA

Requirements
Must have
• Must have my company logo
Should not have
• No photos or complex graphics

```html
<!DOCTYPE html>
<html lang="en">
<head>
<meta charset="utf-8">
<title>Thornwell Building Company – Sign</title>
<link href="https://fonts.googleapis.com/css2?family=Montserrat:wght@600;700;900&display=swap" rel="stylesheet">
<style>
  :root {
    --navy: #1b1e6b;
    --green: #6ab12f;
    --white: #ffffff;
    --ink: #0d0d0d;
    --backdrop: #b6b6b6;
  }
  html, body {
    margin: 0;
    width: 1200px;
    height: 1200px;
    overflow: hidden;
    background: var(--backdrop);
    font-family: "Montserrat", sans-serif;
  }
  .sign {
    position: absolute;
    left: 50px;
    top: 325px;
    width: 1100px;
    height: 550px;
    overflow: hidden;
    background: var(--navy);
  }
  .sign-shapes {
    position: absolute;
    inset: 0;
  }
  .brand {
    position: absolute;
    left: 40px;
    top: 108px;
    width: 480px;
    text-align: center;
    color: var(--white);
  }
  .brand-mark {
    width: 74px;
    height: 74px;
    margin: 0 auto 14px;
    background: var(--green);
  }
  .brand-estd {
    position: absolute;
    top: 54px;
    font-size: 14px;
    font-weight: 600;
    letter-spacing: 4px;
    line-height: 1;
    color: var(--white);
  }
  .brand-estd.left { left: 30px; }
  .brand-estd.right { right: 30px; }
  .brand-name {
    margin: 0;
    font-weight: 700;
    color: var(--white);
    line-height: 1;
  }
  .brand-name .line-main {
    display: block;
    font-size: 56px;
    letter-spacing: 1px;
  }
  .brand-name .line-sub {
    display: block;
    margin-top: 10px;
    font-size: 23px;
    letter-spacing: 7px;
  }
  .brand-phone {
    margin-top: 18px;
    font-size: 24px;
    font-weight: 600;
    letter-spacing: 4px;
  }
  .headline {
    position: absolute;
    left: 585px;
    top: 78px;
    width: 510px;
    margin: 0;
    text-align: center;
    font-weight: 900;
    line-height: 1;
  }
  .headline span { display: block; }
  .headline .word-build { color: var(--green); font-size: 82px; letter-spacing: 5px; }
  .headline .word-with { color: var(--ink); font-size: 54px; letter-spacing: 6px; margin-top: 6px; }
  .headline .word-crew { color: var(--navy); font-size: 78px; margin-top: 4px; }
  .license {
    position: absolute;
    left: 548px;
    top: 354px;
    font-size: 12px;
    font-weight: 700;
    letter-spacing: 5px;
    line-height: 1;
    white-space: nowrap;
    color: var(--white);
  }
  .contact-web, .contact-mail {
    position: absolute;
    color: var(--white);
    font-weight: 700;
    white-space: nowrap;
  }
  .contact-web { left: 270px; top: 424px; font-size: 31px; }
  .contact-mail { left: 135px; top: 470px; font-size: 37px; }
</style>
</head>
<body>
  <div class="sign">
    <svg class="sign-shapes" width="1100" height="550" viewBox="0 0 1100 550" aria-hidden="true">
      <polygon points="315,0 834,0 820,21 330,21" fill="var(--green)"/>
      <path d="M605,49 H1080 L1100,70 V400 H745 L712,333 H578 V76 Q578,49 605,49 Z" fill="var(--white)"/>
      <path d="M0,333 H712 L745,400 H1100 V532 H0 Z" fill="var(--green)"/>
      <polygon points="110,333 482,333 440,402 150,402" fill="var(--navy)"/>
      <rect x="925" y="385" width="175" height="3" fill="var(--navy)"/>
      <rect x="0" y="440" width="260" height="3" fill="var(--white)"/>
      <rect x="0" y="532" width="1100" height="18" fill="var(--navy)"/>
    </svg>

    <div class="brand">
      <div class="brand-mark"></div>
      <span class="brand-estd left">ESTD</span>
      <span class="brand-estd right">2020</span>
      <h1 class="brand-name">
        <span class="line-main">THORNWELL</span>
        <span class="line-sub">BUILDING COMPANY</span>
      </h1>
      <div class="brand-phone">472.555.0188</div>
    </div>

    <h2 class="headline">
      <span class="word-build">BUILD</span>
      <span class="word-with">WITH THE</span>
      <span class="word-crew">T-CREW!</span>
    </h2>

    <div class="license">Lic#4620385</div>
    <div class="contact-web">thornwellbuildingcompany.com</div>
    <div class="contact-mail">thornwellbuildingcompany@mailvero.com</div>
  </div>
</body>
</html>
```